Marlowe Holdings LLC - Business Cards

Need the following information on the cards:

Name: Dean R Vossler
Title: Chief Executive Manager

Business address:
412 N Ridgeview Lane #118
Carol Stream, Il 60412

Phone: (630) 555-0148 - Business
KPV FFL license number: 5-21-xxx-xx-xx-04519
Email: dean.vossler@marloweholdingsffl.com

Target Market(s)

Firearm owners

Industry/Entity Type

Firearms industry,

Contact Information for Business Card

Contact number, name and title, web page address, email, business address and kpv license number,

Requirements
Must have
• Name, title, business address, phone numbers, KPV license numbers, web page address and email address.
Nice to have
• Cellphone number,

```html
<!DOCTYPE html>
<html lang="en">
<head>
<meta charset="utf-8">
<title>Marlowe Holdings LLC – Business Cards</title>
<link rel="stylesheet" href="https://fonts.googleapis.com/css2?family=Cinzel:wght@500;700&family=Josefin+Sans:wght@700&family=Montserrat:wght@600;700&display=swap">
<style>
  :root {
    --brand-red: #b3151c;
    --bright-red: #d3262b;
    --ink: #111111;
    --card-black: #1b1b1b;
    --edge-grey: #6d6d6d;
    --paper: #ffffff;
  }
  * { margin: 0; padding: 0; box-sizing: border-box; }
  html, body { width: 998px; height: 1200px; overflow: hidden; background: var(--paper); }
  .sheet { position: relative; width: 998px; height: 1200px; }

  .brand-name {
    position: absolute;
    font-family: "Josefin Sans", sans-serif;
    font-weight: 700;
    text-align: center;
    letter-spacing: 2px;
    line-height: 1.1;
  }

  /* Front card */
  .front { position: absolute; left: 0; top: 0; width: 998px; height: 600px; background: var(--paper); }
  .front .brand-name { left: 30px; top: 222px; width: 340px; font-size: 40px; color: var(--brand-red); }

  .target-icon { position: absolute; left: 480px; top: 134px; }

  .contact { position: absolute; right: 65px; top: 140px; text-align: right; font-family: "Cinzel", serif; font-weight: 500; color: var(--ink); }
  .person-name { font-size: 40px; font-weight: 700; color: var(--brand-red); line-height: 1; letter-spacing: 1px; }
  .person-title { font-size: 23px; letter-spacing: 3px; margin-top: 4px; }
  .license-label { font-size: 15px; letter-spacing: 2px; color: var(--brand-red); margin-top: 14px; }
  .license-number { font-family: "Montserrat", sans-serif; font-weight: 700; font-size: 20px; color: var(--brand-red); line-height: 1.1; }
  .address { font-size: 25px; letter-spacing: 3.5px; line-height: 31px; margin-top: 16px; }
  .phone { font-size: 25px; letter-spacing: 3px; margin-top: 2px; }
  .phone-number { font-family: "Montserrat", sans-serif; font-weight: 700; font-size: 30px; letter-spacing: 0; }
  .email { font-size: 16px; letter-spacing: 2.5px; margin-top: 4px; }

  .front-band {
    position: absolute; left: 0; top: 465px; width: 760px; height: 135px;
    background: linear-gradient(90deg, var(--brand-red) 0%, var(--brand-red) 55%, rgba(179,21,28,0.55) 100%);
  }

  /* Back card */
  .back { position: absolute; left: 0; top: 600px; width: 998px; height: 600px; background: var(--card-black); border: 6px solid var(--edge-grey); border-top: 2px solid var(--edge-grey); overflow: hidden; }
  .back .brand-name { left: 243px; top: 205px; width: 500px; font-size: 54px; color: var(--paper); }
  .website {
    position: absolute; left: 193px; top: 440px; width: 680px; text-align: center;
    font-family: "Montserrat", sans-serif; font-weight: 600; font-size: 31px; color: var(--bright-red); letter-spacing: 2px;
  }
  .back-band {
    position: absolute; left: -6px; top: 494px; width: 766px; height: 110px;
    background: linear-gradient(90deg, var(--bright-red) 0%, var(--bright-red) 55%, rgba(211,38,43,0.55) 100%);
  }
</style>
</head>
<body>
<div class="sheet">

  <section class="front">
    <div class="brand-name">MARLOWE<br>HOLDINGS LLC</div>

    <svg class="target-icon" width="66" height="66" viewBox="0 0 66 66" aria-hidden="true">
      <circle cx="33" cy="33" r="20" fill="none" stroke="var(--brand-red)" stroke-width="2.5"/>
      <circle cx="33" cy="33" r="11" fill="none" stroke="var(--brand-red)" stroke-width="2"/>
      <line x1="33" y1="2" x2="33" y2="64" stroke="var(--brand-red)" stroke-width="2"/>
      <line x1="2" y1="33" x2="64" y2="33" stroke="var(--brand-red)" stroke-width="2"/>
    </svg>

    <div class="contact">
      <div class="person-name">Dean R. Vossler</div>
      <div class="person-title">Chief Executive Manager</div>
      <div class="license-label">KPV FFL license number:</div>
      <div class="license-number">5-21-xxx-xx-xx-04519</div>
      <div class="address">412 N Ridgeview Lane #118<br>Carol Stream, Il 60412</div>
      <div class="phone"><span class="phone-number">(630) 555-0148</span> - Business</div>
      <div class="email">dean.vossler@marloweholdingsffl.com</div>
    </div>

    <div class="front-band" role="img" aria-label="Distressed red band with diagonal stripes"></div>
  </section>

  <section class="back">
    <div class="brand-name">MARLOWE<br>HOLDINGS LLC</div>
    <div class="website">WWW.MARLOWEHOLDINGSFFL.COM</div>
    <div class="back-band" role="img" aria-label="Distressed red band with diagonal stripes"></div>
  </section>

</div>
</body>
</html>
```